Visitenkarten für eine Hypnose-Praxis
Ich bin sehr zufrieden mit der professionellen Arbeitsweise von KOR7342. Es war immer ein netter Kontakt und meine Wünsche wurden schnell umgesetzt. Alle Vorschläge waren sehr kreativ und und so viel es mir leicht, eine schnelle Entscheidung zu treffen.
Zielgruppe
Wir sind eine Hypnose-Praxis und richten unser Angebot an Privatpersonen unterschiedlichen Alters, die therapeutische Unterstützung suchen.
Aufgabenstellung
Eher schlichtes und modernes Design

```html
<!DOCTYPE html>
<html lang="de">
<head>
<meta charset="utf-8">
<title>Visitenkarten – wolkenleicht</title>
<link rel="stylesheet" href="https://fonts.googleapis.com/css2?family=Roboto:wght@300;400;500&display=swap">
<style>
  :root {
    --bg: #efefef;
    --paper: #ffffff;
    --ink: #2b2b2b;
    --ink-soft: #8a8a8a;
    --teal: #12b8aa;
    --teal-light: #2cc4b4;
    --square: #3aa9c9;
  }
  * { box-sizing: border-box; margin: 0; padding: 0; }
  html, body {
    width: 1200px; height: 929px; overflow: hidden;
    background: var(--bg);
    font-family: "Roboto", Arial, sans-serif;
    color: var(--ink);
  }
  .stage {
    position: relative; width: 1200px; height: 929px;
    display: flex; justify-content: center; align-items: center; gap: 40px;
  }
  .card {
    position: relative; width: 520px; height: 336px;
    background: var(--paper);
    box-shadow: 0 10px 30px rgba(0,0,0,0.12), 0 2px 4px rgba(0,0,0,0.08);
    overflow: hidden;
  }
  .card__band {
    position: absolute; left: 0; right: 0; bottom: 0; height: 16px;
    background: linear-gradient(90deg, var(--teal), var(--teal-light));
  }
  .brand {
    position: absolute; display: flex; align-items: center; gap: 12px;
  }
  .brand__square {
    width: 30px; height: 30px; border-radius: 5px; background: var(--square);
  }
  .brand__name {
    font-weight: 400; color: var(--ink); letter-spacing: 0.5px;
  }
  /* Front */
  .card--front .brand { top: 48px; left: 230px; }
  .card--front .brand__name { font-size: 38px; }
  .person-name {
    position: absolute; left: 36px; top: 122px;
    font-size: 27px; font-weight: 400; letter-spacing: 1.5px; text-transform: uppercase;
  }
  .divider {
    position: absolute; left: 250px; top: 170px; width: 1px; height: 48px;
    background: var(--teal);
  }
  .credentials {
    position: absolute; left: 268px; top: 170px; width: 240px;
    font-size: 9.5px; font-weight: 300; color: var(--ink-soft); line-height: 1.45;
  }
  .contact {
    position: absolute; left: 268px; top: 218px;
    font-size: 12.5px; line-height: 1.55; list-style: none;
  }
  .address {
    position: absolute; left: 36px; top: 292px;
    font-size: 12.5px;
  }
  /* Back */
  .card--back .brand { top: 50%; left: 50%; transform: translate(-50%, -58%); gap: 16px; }
  .card--back .brand__square { width: 40px; height: 40px; border-radius: 7px; }
  .card--back .brand__name { font-size: 54px; }
</style>
</head>
<body>
<main class="stage">
  <article class="card card--front">
    <div class="brand">
      <span class="brand__square"></span>
      <span class="brand__name">wolkenleicht</span>
    </div>
    <h1 class="person-name">Lena Morwitz</h1>
    <span class="divider"></span>
    <p class="credentials">Diplom-Psychologin, Heilpraktikerin für Psychotherapie<br>mit Spezialisierung Hypnose-Therapie</p>
    <ul class="contact">
      <li>Telefon: 030 5550 1287</li>
      <li>24-Std-AB: 030 5550 4462</li>
      <li>info@wolkenleicht-praxis.de</li>
      <li>www.wolkenleicht-praxis.de</li>
    </ul>
    <p class="address">Birkenweg 14, 10115 Berlin</p>
    <span class="card__band"></span>
  </article>

  <article class="card card--back">
    <div class="brand">
      <span class="brand__square"></span>
      <span class="brand__name">wolkenleicht</span>
    </div>
    <span class="card__band"></span>
  </article>
</main>
</body>
</html>
```